updated design and flyer

Can you make this into a TRI FOLD design?
We would like the words "Call Dorian" take off and changed to Call us
We would like to add Check out our website at CopperMesaHomeInspectionsTX.com
Please delete the home inspections starting as low at $350.00 and change to " you can now book with us on- line "

```html
<!DOCTYPE html>
<html lang="en">
<head>
<meta charset="utf-8">
<title>Copper Mesa Home Inspections – Tri-fold</title>
<link href="https://fonts.googleapis.com/css2?family=Montserrat:wght@300;400;500;700;800&display=swap" rel="stylesheet">
<style>
  :root{
    --red:#b52228;
    --red-dark:#870b0e;
    --navy:#1b3a6b;
    --navy-deep:#0a1634;
    --band-dark:#170d17;
    --white:#ffffff;
    --page:#ffffff;
  }
  html,body{margin:0;padding:0;width:1200px;height:1200px;overflow:hidden;background:var(--page);}
  body{font-family:'Montserrat',sans-serif;position:relative;}
  .brochure{position:absolute;left:107px;top:193px;width:961px;height:743px;overflow:hidden;}
  .brochure-shapes{position:absolute;left:0;top:0;width:961px;height:743px;}
  .abs{position:absolute;}

  .service-star{left:18px;width:19px;height:19px;fill:var(--white);}
  .service-title{left:46px;margin:0;color:var(--white);font-weight:700;font-size:15.5px;letter-spacing:-0.3px;white-space:nowrap;}
  .service-text{left:46px;width:252px;margin:0;color:var(--white);font-weight:400;font-size:12.4px;line-height:16px;letter-spacing:0.2px;}

  .contact{left:310px;width:343px;text-align:center;color:var(--white);}
  .call-title{margin:0;font-weight:700;font-size:25px;}
  .call-number{margin:0;font-weight:400;font-size:32.5px;letter-spacing:-0.5px;}
  .contact-icon{display:block;margin:0 auto;stroke:var(--white);fill:none;stroke-width:2;}
  .contact-label{margin:0;font-weight:700;font-size:12.5px;}
  .contact-value{margin:0;font-weight:400;font-size:12.5px;}
  .booking-note{margin:0;font-weight:700;font-size:12.5px;}
  .website-note{margin:0;font-weight:400;font-size:12px;line-height:16px;}

  .brand{left:678px;top:423px;display:flex;align-items:center;gap:8px;}
  .brand-dot{width:14px;height:14px;border-radius:50%;background:var(--navy);}
  .brand-name{color:var(--navy);font-weight:500;font-size:21px;letter-spacing:0.3px;white-space:nowrap;}

  .headline{left:678px;top:496px;margin:0;font-size:29px;line-height:33px;letter-spacing:-0.4px;white-space:nowrap;}
  .headline span{display:block;}
  .headline .light{font-weight:300;color:var(--navy);}
  .headline .bold{font-weight:700;color:var(--navy);}
  .headline .accent{font-weight:300;color:var(--red);}
</style>
</head>
<body>
<main class="brochure">
  <svg class="brochure-shapes" viewBox="0 0 1538 1188" preserveAspectRatio="none">
    <defs>
      <linearGradient id="houseTop" x1="0" y1="0" x2="1" y2="1">
        <stop offset="0" stop-color="#5f7d45"/>
        <stop offset="0.45" stop-color="#a07f6e"/>
        <stop offset="1" stop-color="#8a6d5d"/>
      </linearGradient>
      <linearGradient id="houseBottom" x1="0" y1="0" x2="0" y2="1">
        <stop offset="0" stop-color="#9cc0e6"/>
        <stop offset="0.45" stop-color="#a58e76"/>
        <stop offset="1" stop-color="#4e7a3a"/>
      </linearGradient>
      <clipPath id="bluePanel"><rect x="495" y="0" width="549" height="1188"/></clipPath>
    </defs>

    <rect class="panel-services" x="0" y="0" width="495" height="1188" fill="var(--red)"/>
    <rect class="panel-contact" x="495" y="0" width="549" height="1188" fill="var(--navy)"/>
    <rect class="panel-cover" x="1044" y="0" width="494" height="1188" fill="var(--white)"/>

    <path class="cover-photo" role="img" aria-label="Photo of a two-storey brick house with trees"
      d="M690,0 L1538,0 L1538,500 L1410,628 Q1374,664 1338,628 Z" fill="url(#houseTop)"/>
    <path class="accent-band-top" d="M575,0 L690,0 L960,262 Q905,320 855,280 Z" fill="var(--navy-deep)"/>
    <path class="accent-red-right" d="M1538,445 L1420,563 Q1395,595 1425,625 L1538,740 Z" fill="var(--red)"/>
    <path class="accent-red-corner" d="M1538,1040 Q1490,1030 1460,1065 L1340,1188 L1538,1188 Z" fill="var(--red)"/>

    <path class="services-photo" role="img" aria-label="Photo of a brick and stone family home with a front garden"
      d="M0,985 L190,822 Q224,790 258,822 L636,1188 L0,1188 Z" fill="url(#houseBottom)"/>
    <path class="accent-band-bottom" d="M300,862 Q353,812 405,862 L729,1188 L636,1188 Z" fill="var(--red-dark)"/>
    <path class="accent-band-bottom-dark" clip-path="url(#bluePanel)" d="M300,862 Q353,812 405,862 L729,1188 L636,1188 Z" fill="var(--band-dark)"/>
  </svg>

  <!-- Services -->
  <svg class="abs service-star" style="top:53px" viewBox="0 0 24 24"><path d="M12 1l3.2 7.2 7.8.7-5.9 5.2 1.8 7.7L12 17.8 5.1 21.8l1.8-7.7L1 8.9l7.8-.7z"/></svg>
  <h2 class="abs service-title" style="top:53px">Pre-Purchase Home Inspection</h2>
  <p class="abs service-text" style="top:85px">Ensure that the home you are considering meets your expectations and identify any potential issues before making a purchase.</p>

  <svg class="abs service-star" style="top:205px" viewBox="0 0 24 24"><path d="M12 1l3.2 7.2 7.8.7-5.9 5.2 1.8 7.7L12 17.8 5.1 21.8l1.8-7.7L1 8.9l7.8-.7z"/></svg>
  <h2 class="abs service-title" style="top:205px">Pre-Listing Home Inspection</h2>
  <p class="abs service-text" style="top:237px">Get a thorough evaluation of your property's condition before listing it for sale, allowing you to address any necessary repairs beforehand.</p>

  <svg class="abs service-star" style="top:359px" viewBox="0 0 24 24"><path d="M12 1l3.2 7.2 7.8.7-5.9 5.2 1.8 7.7L12 17.8 5.1 21.8l1.8-7.7L1 8.9l7.8-.7z"/></svg>
  <h2 class="abs service-title" style="top:359px">New Construction Inspection</h2>
  <p class="abs service-text" style="top:391px">Verify the quality and craftsmanship of your newly built home, ensuring it meets industry standards and your expectations.</p>

  <!-- Contact -->
  <div class="abs contact" style="top:225px">
    <p class="call-title">CALL US</p>
    <p class="call-number" style="margin-top:4px">(555)014-2287</p>
  </div>

  <div class="abs contact" style="top:330px">
    <svg class="contact-icon" width="23" height="23" viewBox="0 0 24 24"><circle cx="12" cy="12" r="10"/><path d="M12 6v6l3.5 3.5"/></svg>
    <p class="contact-label" style="margin-top:5px">Business Hours</p>
    <p class="contact-value" style="margin-top:3px">Monday - Sunday 9AM - 6PM</p>
  </div>

  <div class="abs contact" style="top:418px">
    <svg class="contact-icon" width="21" height="17" viewBox="0 0 24 18"><rect x="1" y="1" width="22" height="16" rx="1.5" fill="var(--white)" stroke="none"/><path d="M2 2l10 8 10-8" stroke="var(--navy)"/></svg>
    <p class="contact-label" style="margin-top:6px">Email</p>
    <p class="contact-value" style="margin-top:3px">Coppermesahomeinspectionstx@mail.com</p>
  </div>

  <div class="abs contact" style="top:498px">
    <svg class="contact-icon" width="22" height="28" viewBox="0 0 24 30"><path d="M12 2a9 9 0 0 0-9 9c0 6 9 13 9 13s9-7 9-13a9 9 0 0 0-9-9z"/><circle cx="12" cy="11" r="3.5" fill="var(--white)" stroke="none"/><path d="M6 28h12"/></svg>
    <p class="contact-label" style="margin-top:6px">Service Area</p>
    <p class="contact-value" style="margin-top:3px">Serving The Woodlands &amp; Surrounding Areas</p>
  </div>

  <div class="abs contact" style="top:572px">
    <p class="booking-note">You can now book with us online</p>
    <p class="website-note" style="margin-top:6px">Check out our website at<br>CopperMesaHomeInspectionsTX.com</p>
  </div>

  <!-- Cover -->
  <div class="abs brand">
    <span class="brand-dot"></span>
    <span class="brand-name">COPPER MESA</span>
  </div>

  <h1 class="abs headline">
    <span class="light">Professional</span>
    <span class="bold">Home</span>
    <span class="bold">Inspections</span>
    <span class="accent">in The Woodlands</span>
  </h1>
</main>
</body>
</html>
```